Bref créative
Business Cards for Young Professional
Professional, edgy, modern, credible, smart.
Professional
Doran Whitlake
Owner
4627 Mesa Lorna, NW
Albuquerque, NM 87309
dorenw@velbrik.example
velbrik.example
I plan to have cards printed on paper. But some will be made by metal etching. These metal cards will have a small area to be filled with melted brazing metal. I will attach pictures to demonstrate this principal.

```html
<!DOCTYPE html>
<html lang="en">
<head>
<meta charset="utf-8">
<title>Pelimarker Consolidated — Business Card</title>
<link href="https://fonts.googleapis.com/css2?family=Michroma&family=Montserrat:wght@400;500;600&display=swap" rel="stylesheet">
<style>
  :root {
    --backdrop: #d9dadc;
    --card: #ffffff;
    --card-shade: #f1f2f4;
    --blue: #1b2f9c;
    --blue-deep: #0d1a6e;
    --blue-light: #3d56d4;
    --silver: #b9bcc2;
    --silver-dark: #7c8088;
    --ink: #4a4d55;
    --ink-soft: #8a8d94;
  }
  * { box-sizing: border-box; margin: 0; padding: 0; }
  html, body { width: 1200px; height: 984px; overflow: hidden; }
  body {
    background: var(--backdrop);
    font-family: "Montserrat", Arial, sans-serif;
    position: relative;
  }
  .card {
    position: absolute;
    width: 700px;
    height: 400px;
    border-radius: 26px;
    background: linear-gradient(160deg, var(--card) 0%, var(--card) 60%, var(--card-shade) 100%);
    box-shadow: 0 14px 30px rgba(0,0,0,0.18);
    overflow: hidden;
  }
  /* Front card */
  .card--front { left: 110px; top: 62px; }
  .front-mark {
    position: absolute;
    left: 50%; top: 50%;
    transform: translate(-50%, -50%);
    display: flex; flex-direction: column; align-items: center; gap: 18px;
  }
  .mark-dot {
    width: 90px; height: 90px; border-radius: 50%;
    background: var(--blue);
  }
  .mark-name {
    font-family: "Michroma", sans-serif;
    font-size: 22px;
    letter-spacing: 3px;
    color: var(--blue);
  }
  .front-web {
    position: absolute;
    left: 34px; top: 50%;
    transform: translate(-50%, -50%) rotate(-90deg);
    transform-origin: center;
    font-family: "Michroma", sans-serif;
    font-size: 11px;
    letter-spacing: 9px;
    color: var(--silver-dark);
    white-space: nowrap;
    margin-left: 30px;
  }
  /* Back card */
  .card--back { left: 390px; top: 510px; }
  .brand {
    position: absolute; left: 44px; top: 34px;
    display: flex; align-items: center; gap: 16px;
  }
  .brand-dot { width: 62px; height: 62px; border-radius: 50%; background: var(--blue); }
  .brand-name {
    font-family: "Michroma", sans-serif;
    font-size: 19px; letter-spacing: 1px;
    color: var(--blue);
  }
  .brand-tag {
    font-size: 9px; letter-spacing: 4px; text-transform: uppercase;
    color: var(--ink-soft); margin-top: 5px; text-align: right;
  }
  .holder {
    position: absolute; left: 160px; top: 122px;
    font-variant: small-caps;
    letter-spacing: 2px;
    color: var(--ink);
    font-size: 16px;
  }
  .holder .person { font-weight: 600; }
  .holder .role { color: var(--ink-soft); }
  .address {
    position: absolute; left: 160px; top: 168px;
    font-variant: small-caps; letter-spacing: 2px;
    font-size: 15px; line-height: 1.45; color: var(--ink);
  }
  .contacts {
    position: absolute; left: 420px; top: 168px;
    list-style: none; font-size: 13px; letter-spacing: 1px;
    color: var(--ink); line-height: 1;
  }
  .contacts li { display: flex; align-items: center; gap: 8px; margin-bottom: 8px; }
  .contacts svg { width: 16px; height: 16px; flex: none; }
  .wave { position: absolute; left: 0; bottom: 0; width: 700px; height: 170px; }
</style>
</head>
<body>

<section class="card card--front" aria-label="Card front">
  <div class="front-web">WWW.VELBRIK.EXAMPLE</div>
  <div class="front-mark">
    <span class="mark-dot"></span>
    <span class="mark-name">PELIMARKER</span>
  </div>
</section>

<section class="card card--back" aria-label="Card back">
  <div class="brand">
    <span class="brand-dot"></span>
    <div>
      <div class="brand-name">PELIMARKER CONSOLIDATED</div>
      <div class="brand-tag">Industrial Services</div>
    </div>
  </div>

  <div class="holder"><span class="person">Doran Whitlake</span>, <span class="role">Owner</span></div>

  <address class="address" style="font-style:normal">
    4627 Mesa Lorna,<br>NW Albuquerque,<br>NM 87309
  </address>

  <ul class="contacts">
    <li>
      <svg viewBox="0 0 16 16"><circle cx="8" cy="8" r="8" fill="var(--blue-deep)"/><path d="M5.3 4.2l1.4-.3.8 2-1 .7c.4 1 1.2 1.8 2.2 2.2l.7-1 2 .8-.3 1.4c-3.4.2-6-2.4-5.8-5.8z" fill="#fff"/></svg>
      505-555-0147
    </li>
    <li>
      <svg viewBox="0 0 16 16"><circle cx="8" cy="8" r="8" fill="var(--blue-deep)"/><rect x="4" y="5" width="8" height="6" fill="none" stroke="#fff" stroke-width="1"/><path d="M4 5l4 3.2L12 5" fill="none" stroke="#fff" stroke-width="1"/></svg>
      dorenw@velbrik.example
    </li>
    <li>
      <svg viewBox="0 0 16 16"><circle cx="8" cy="8" r="8" fill="var(--blue-deep)"/><circle cx="8" cy="8" r="4.2" fill="none" stroke="#fff" stroke-width="1"/><path d="M3.8 8h8.4M8 3.8c-2 2.4-2 6 0 8.4M8 3.8c2 2.4 2 6 0 8.4" fill="none" stroke="#fff" stroke-width=".8"/></svg>
      www.velbrik.example
    </li>
  </ul>

  <svg class="wave" viewBox="0 0 700 170" preserveAspectRatio="none" aria-hidden="true">
    <defs>
      <linearGradient id="bandBlue" x1="0" y1="0" x2="1" y2="1">
        <stop offset="0" stop-color="var(--blue-light)"/>
        <stop offset="0.5" stop-color="var(--blue)"/>
        <stop offset="1" stop-color="var(--blue-deep)"/>
      </linearGradient>
      <linearGradient id="bandSilver" x1="0" y1="0" x2="1" y2="0">
        <stop offset="0" stop-color="#e6e7ea"/>
        <stop offset="0.5" stop-color="var(--silver)"/>
        <stop offset="1" stop-color="var(--silver-dark)"/>
      </linearGradient>
    </defs>
    <path d="M0 40 C160 120 420 150 700 20 L700 170 L0 170 Z" fill="url(#bandSilver)"/>
    <path d="M0 58 C170 135 430 160 700 38 L700 170 L0 170 Z" fill="url(#bandBlue)"/>
  </svg>
</section>

</body>
</html>
```